Velvor IT Services Business Card

Velvor IT Services are a Perth based IT Services company. We would like to incorporate our company logo (attached) and stick with the blue that is in that design. I would like a clean look design that isn't too busy, yet creates a lasting image that is instantly recognisable in the recipients mind.

Target Market(s)

The target audience is small/medium business owners.

Industry/Entity Type

Business

Font styles to use
Serif
Sans Serif

Colors

Designer to choose colors to be used in the design.

Requirements
Must have
• The design should include:
Business name: Velvor IT Services
Directors Name: Marcus Dredge
Phone Number: 0483 906 452
Email: support@velvorit.com.au
Website: www.velvorit.com.au

```html
<!DOCTYPE html>
<html lang="en">
<head>
<meta charset="utf-8">
<title>Velvor IT Services Business Card</title>
<link rel="stylesheet" href="https://fonts.googleapis.com/css2?family=Arimo:wght@400;700&display=swap">
<style>
  :root {
    --page: #ffffff;
    --frame: #2b2b2b;
    --band: #c4c4c4;
    --rule: #ffffff;
    --face-light: #ffffff;
    --face-mid: #e6e6e8;
    --face-edge: #c9c9cc;
    --tile: #e3e3e3;
    --brand-blue: #3d9ddb;
    --brand-deep: #1c5fa8;
    --ink: #2a2a2a;
    --label: #333333;
    --line: #1a1a1a;
  }
  * { box-sizing: border-box; margin: 0; padding: 0; }
  html, body {
    width: 1064px; height: 1200px; overflow: hidden;
    background: var(--page);
    font-family: "Arimo", Arial, sans-serif;
  }
  .canvas { position: relative; width: 1064px; height: 1200px; }

  .card {
    position: absolute; left: 38px; width: 915px;
    background: var(--frame);
  }
  .card--front { top: 38px; height: 515px; }
  .card--back { top: 632px; height: 543px; }

  .side-label {
    position: absolute; left: 970px;
    font-size: 26px; color: var(--label);
  }
  .side-label--front { top: 552px; }
  .side-label--back { top: 1140px; }

  /* Front */
  .front-band {
    position: absolute; inset: 24px;
    background: var(--band);
  }
  .front-face {
    position: absolute; inset: 9px;
    border: 3px solid var(--rule);
    background: radial-gradient(ellipse at 50% 45%, var(--face-light) 0%, var(--face-mid) 60%, var(--face-edge) 100%);
    display: flex; align-items: center; justify-content: center;
  }
  .brand {
    display: flex; align-items: center; gap: 22px;
    transform: translateY(-6px);
  }
  .brand-mark {
    width: 58px; height: 58px; background: var(--brand-deep);
  }
  .brand-name {
    font-weight: 700; font-size: 60px; color: var(--brand-deep);
    letter-spacing: 1px;
  }

  /* Back */
  .back-face {
    position: absolute; inset: 26px;
    background: var(--page);
  }
  .back-rule {
    position: absolute; inset: 14px;
    border: 2px solid var(--line);
  }
  .contact-tile {
    position: absolute; left: 68px; width: 421px; height: 123px;
    background: var(--tile);
    display: flex; align-items: center;
  }
  .contact-tile--phone { top: 70px; }
  .contact-tile--email { top: 207px; }
  .contact-tile--web { top: 345px; }
  .contact-icon {
    margin-left: 21px; width: 74px; height: 74px;
    background: var(--brand-blue);
    display: flex; align-items: center; justify-content: center;
    flex-shrink: 0;
  }
  .contact-icon svg { width: 36px; height: 36px; }
  .contact-text {
    margin-left: 14px; font-size: 23px; color: var(--ink);
    white-space: nowrap;
  }
  .name-panel {
    position: absolute; left: 502px; top: 70px; width: 332px; height: 398px;
    background: var(--brand-blue);
  }
  .name-panel-inner {
    position: absolute; inset: 12px;
    border: 4px solid var(--rule);
    display: flex; flex-direction: column; align-items: center; justify-content: center;
    color: #ffffff; text-align: center;
  }
  .person-name { font-size: 28px; }
  .person-role { font-size: 22px; margin-top: 4px; }
</style>
</head>
<body>
<div class="canvas">

  <section class="card card--front">
    <div class="front-band">
      <div class="front-face">
        <div class="brand">
          <span class="brand-mark"></span>
          <span class="brand-name">Velvor IT Services</span>
        </div>
      </div>
    </div>
  </section>
  <span class="side-label side-label--front">Front</span>

  <section class="card card--back">
    <div class="back-face">
      <div class="back-rule"></div>

      <div class="contact-tile contact-tile--phone">
        <span class="contact-icon">
          <svg viewBox="0 0 24 24" aria-hidden="true"><path fill="#fff" d="M6.6 10.8c1.4 2.8 3.8 5.1 6.6 6.6l2.2-2.2c.3-.3.7-.4 1-.2 1.1.4 2.3.6 3.6.6.6 0 1 .4 1 1V20c0 .6-.4 1-1 1C10.6 21 3 13.4 3 4c0-.6.4-1 1-1h3.5c.6 0 1 .4 1 1 0 1.3.2 2.5.6 3.6.1.3 0 .7-.2 1l-2.3 2.2z"/></svg>
        </span>
        <span class="contact-text">0483 906 452</span>
      </div>

      <div class="contact-tile contact-tile--email">
        <span class="contact-icon">
          <svg viewBox="0 0 24 24" aria-hidden="true"><rect x="3" y="6" width="18" height="12" fill="#fff"/><path d="M3 6l9 7 9-7" fill="none" stroke="#3d9ddb" stroke-width="1.4"/></svg>
        </span>
        <span class="contact-text">support@velvorit.com.au</span>
      </div>

      <div class="contact-tile contact-tile--web">
        <span class="contact-icon">
          <svg viewBox="0 0 24 24" aria-hidden="true" fill="none" stroke="#fff" stroke-width="1.6"><circle cx="12" cy="12" r="9"/><ellipse cx="12" cy="12" rx="4" ry="9"/><path d="M3 12h18M5 7.5h14M5 16.5h14"/></svg>
        </span>
        <span class="contact-text">www.velvorit.com.au</span>
      </div>

      <div class="name-panel">
        <div class="name-panel-inner">
          <span class="person-name">Marcus Dredge</span>
          <span class="person-role">Director</span>
        </div>
      </div>
    </div>
  </section>
  <span class="side-label side-label--back">Back</span>

</div>
</body>
</html>
```